Business card design needed

Family General Practitioner/ Family Physician.
Logo is the logo of the Crestmoor Guild of Family Clinicians Australia
http://kvplm.tarevo.edu.au/PictureGallery/logos/pages/CGFC%20logo_jpg.htm

Reason: Just a bit more time to make changes and the weekend for me to look at things closely and to choose. Thanks, Lumi

Thanks for all the submissions. So many of them are really works of art. Not one of them are not good. The ones that I am eliminating are the ones that I think are not suitable for me personally only, and because if I don't, it makes it very difficult to decide as many of you are also sending me slight variations of a card. I have just decided to choose a second place card too. Can't thank you all enough. Good luck, Lumi. P.S - Working today till 10 pm as the card says :-), so probably won't be able to give a feedback till late Saturday night or Sunday morning here in Sydney, Australia. 

Reason: Just added a second place to the budget and realised that Australia is ahead of the rest of the world in the time zone (only :-) - don't want to offend anyone or start a debate!! ) , so Monday deadline will mean it will be a weekend for the rest of the world. Just wanted to give everyone more time to submit their best, especially since I will be picking a second card too. Can't thank everyone enough for the submissions. P.S - Not keen on photos on the card.

Contact Information for Business Card

Dr. Lumi Harcourt M.B.B.S., F.C.G.F.C
Family General Practitioner
Address, timings, phone and fax number on the back.

Requirements
Must have
• Timings
Mon 7 am - 7 pm
Tues 7 am - 12 pm
Wed 7 am - 10 pm
Thurs 7 am - 12 pm
Fri 7 am - 8 pm
Sat 8 am - 10 pm
Sun - Off

```html
<!DOCTYPE html>
<html lang="en">
<head>
<meta charset="utf-8">
<title>Dr. Lumi Harcourt – Business Card</title>
<link href="https://fonts.googleapis.com/css2?family=Lato:wght@400;700;900&display=swap" rel="stylesheet">
<style>
  :root {
    --backdrop: #e4e6e9;
    --card: #f7f7f7;
    --ink: #111111;
    --swatch-light: #b9b9b9;
    --swatch-mid: #4a4a4a;
    --swatch-dark: #0c0c0c;
    --figures: #8c8c8c;
    --row-1: #0d0d0d;
    --row-2: #151515;
    --row-3: #2c2c2c;
    --row-4: #474747;
    --row-5: #6a6a6a;
    --row-6: #757575;
    --row-7: #868686;
    --row-text: #ffffff;
  }
  * { margin: 0; padding: 0; box-sizing: border-box; }
  html, body {
    width: 1200px; height: 743px; overflow: hidden;
    background: var(--backdrop);
    font-family: "Lato", Arial, sans-serif;
    color: var(--ink);
  }
  .stage { position: relative; width: 1200px; height: 743px; }
  .card {
    position: absolute;
    width: 480px; height: 300px;
    background: var(--card);
    box-shadow: 0 6px 18px rgba(0,0,0,0.18);
    overflow: hidden;
  }
  .card--front { left: 70px; top: 222px; }
  .card--back { left: 650px; top: 222px; }

  /* Front */
  .guild-mark {
    position: absolute; top: 26px; right: 26px;
    display: flex; align-items: center; gap: 6px;
    font-weight: 700; font-size: 15px; letter-spacing: 1px;
  }
  .guild-mark .dot { width: 12px; height: 12px; background: var(--ink); }
  .swatches { position: absolute; right: 0; top: 80px; width: 62px; }
  .swatches span { display: block; height: 32px; }
  .swatches .light { background: var(--swatch-light); }
  .swatches .mid { background: var(--swatch-mid); }
  .swatches .dark { background: var(--swatch-dark); }
  .identity {
    position: absolute; left: 28px; top: 148px;
    font-size: 20px; line-height: 26px; text-transform: uppercase;
    font-weight: 400; letter-spacing: 0.2px;
  }
  .identity strong { font-weight: 900; }
  .family-figures {
    position: absolute; right: 26px; top: 230px;
    width: 124px; height: 38px; background: var(--figures); opacity: 0.55;
  }
  .tagline {
    position: absolute; right: 26px; top: 274px;
    font-size: 12px; font-weight: 400;
  }

  /* Back */
  .contact { position: absolute; left: 28px; top: 56px; font-size: 12.5px; line-height: 16px; }
  .contact dt { font-weight: 900; text-transform: uppercase; }
  .contact dd { margin-bottom: 16px; }
  .hours {
    position: absolute; right: 0; top: 50px; width: 242px;
    border-collapse: separate; border-spacing: 0 7px;
    font-size: 12.5px; color: var(--row-text); text-transform: uppercase;
  }
  .hours td { height: 23px; padding: 0 8px; white-space: nowrap; }
  .hours .day { width: 96px; font-weight: 700; }
  .hours .time { font-weight: 700; }
  .hours tr:nth-child(1) td { background: var(--row-1); }
  .hours tr:nth-child(2) td { background: var(--row-2); }
  .hours tr:nth-child(3) .day { background: var(--row-3); }
  .hours tr:nth-child(3) .time { background: var(--row-2); }
  .hours tr:nth-child(4) .day { background: var(--row-4); }
  .hours tr:nth-child(4) .time { background: var(--row-3); }
  .hours tr:nth-child(5) .day { background: var(--row-5); }
  .hours tr:nth-child(5) .time { background: var(--row-4); }
  .hours tr:nth-child(6) .day { background: var(--row-6); }
  .hours tr:nth-child(6) .time { background: var(--row-4); }
  .hours tr:nth-child(7) .day { background: var(--row-7); }
  .hours tr:nth-child(7) .time { background: var(--row-5); }
</style>
</head>
<body>
<main class="stage">
  <section class="card card--front">
    <div class="guild-mark"><span class="dot"></span>CGFC</div>
    <div class="swatches"><span class="light"></span><span class="mid"></span><span class="dark"></span></div>
    <p class="identity">
      Dr. Lumi <strong>Harcourt</strong><br>
      M. B. B. S. , F.C.G.F.C<br>
      Family <strong>General Practitioner</strong>
    </p>
    <div class="family-figures" role="img" aria-label="Simple line drawing of a family of five stick figures"></div>
    <p class="tagline">caring about your health!</p>
  </section>

  <section class="card card--back">
    <dl class="contact">
      <dt>Address:</dt>
      <dd>Upper Level,<br>Brindle Court,<br>Ashgrove Arcade Shopping Center<br>Fernvale,<br>NSW 2290</dd>
      <dt>Phone:</dt>
      <dd>02 5550 1400</dd>
      <dt>Fax:</dt>
      <dd>02 5550 1433</dd>
    </dl>
    <table class="hours">
      <tr><td class="day">Monday</td><td class="time">07:00 AM - 07:00 PM</td></tr>
      <tr><td class="day">Tuesday</td><td class="time">07:00 AM - 12:00 PM</td></tr>
      <tr><td class="day">Wednesday</td><td class="time">07:00 AM - 10:00 PM</td></tr>
      <tr><td class="day">Thursday</td><td class="time">07:00 AM - 12:00 PM</td></tr>
      <tr><td class="day">Friday</td><td class="time">07:00 AM - 08:00 PM</td></tr>
      <tr><td class="day">Saturday</td><td class="time">08:00 AM - 10:00 PM</td></tr>
      <tr><td class="day">Sunday</td><td class="time">Off</td></tr>
    </table>
  </section>
</main>
</body>
</html>
```